Sticker proposal and a brand name for matured cheese slices

We need a full face sticker design and a brand name for a packaging of cheese slices. The cheese is mature holland gouda (aged for 2-3 months) and lactose free which we want to be addressed. Dimensions of the sticker should be 140x115mm. We want to make up a name for the packages like tavrinco did, but not based on the origin of the cheese. The market we are going to sell at first is the greek one. Our Company is VARNIKO SA and website, varniko-sa.com. The sticker style should be modern, referring to nature, tradition or technology and bright coloured.

Reason: we need more designs to choose from

Target Market(s)

supermarkets

Industry/Entity Type

Food Store

Requirements
Must have
• lactose free, mature, slices
Nice to have
• blue, green colours. a transparent hole so that the cheese slice can be seen. toast/sandwich figure as it is mostly used for sandwich
Should not have
• dark colours

```html
<!DOCTYPE html>
<html lang="en">
<head>
<meta charset="utf-8">
<title>VARNIKO – Lactose free Aged Holland Gouda sticker</title>
<link rel="stylesheet" href="https://fonts.googleapis.com/css2?family=Marcellus&family=Noto+Serif&family=Montserrat:wght@600&display=swap">
<style>
  :root {
    --canvas: #ffffff;
    --paper: #f0f0f0;
    --paper-light: #f6f6f6;
    --white: #ffffff;
    --panel: #efeff1;
    --brand-green: #3aaa35;
    --sky-blue: #29a8e0;
    --ribbon-blue: #2aaae2;
    --ribbon-fold: #1e8cc6;
    --ribbon-text: #f2f4f8;
    --badge: #e6e6e6;
    --cheese-light: #fbeea0;
    --cheese-mid: #f6dd6a;
    --cheese-deep: #eec940;
  }
  html, body {
    margin: 0;
    width: 1200px;
    height: 1093px;
    overflow: hidden;
    background: var(--canvas);
  }
  .sticker {
    position: absolute;
    left: 214px;
    top: 239px;
    width: 807px;
    height: 666px;
  }
  .sticker-art {
    display: block;
    width: 807px;
    height: 666px;
  }
  .brand-name {
    font-family: "Marcellus", serif;
    font-size: 86px;
    fill: var(--brand-green);
    letter-spacing: 2px;
  }
  .claim-lactose {
    font-family: "Noto Serif", serif;
    font-size: 72px;
    fill: var(--sky-blue);
    letter-spacing: 3px;
  }
  .ribbon-title {
    font-family: "Montserrat", sans-serif;
    font-weight: 600;
    fill: var(--ribbon-text);
  }
  .ribbon-title--aged { font-size: 44px; }
  .ribbon-title--variety { font-size: 33px; }
</style>
</head>
<body>
  <main class="sticker">
    <svg class="sticker-art" viewBox="0 0 893 737" xmlns="http://www.w3.org/2000/svg">
      <defs>
        <clipPath id="sticker-edge"><rect x="0" y="0" width="893" height="737"/></clipPath>
        <linearGradient id="cheese-tones" x1="0" y1="0" x2="1" y2="1">
          <stop offset="0" stop-color="var(--cheese-light)"/>
          <stop offset="0.55" stop-color="var(--cheese-mid)"/>
          <stop offset="1" stop-color="var(--cheese-deep)"/>
        </linearGradient>
      </defs>
      <g clip-path="url(#sticker-edge)">
        <rect class="pattern-field" x="0" y="0" width="893" height="737" fill="var(--paper)" role="img" aria-label="Faint traditional ornament pattern"/>
        <ellipse class="swoosh-band" cx="760" cy="460" rx="585" ry="312" fill="var(--paper-light)"/>
        <ellipse class="swoosh-white" cx="760" cy="460" rx="560" ry="290" fill="var(--white)"/>
        <rect x="0" y="441" width="893" height="296" fill="var(--white)"/>
        <circle class="digest-badge" cx="805" cy="258" r="50" fill="none" stroke="var(--badge)" stroke-width="4"/>
        <circle cx="805" cy="258" r="24" fill="var(--badge)"/>
        <rect class="cheese-photo" x="0" y="441" width="629" height="296" fill="url(#cheese-tones)" role="img" aria-label="Rolled slices of gouda cheese with a basil leaf"/>
        <rect class="claim-panel" x="0" y="342" width="563" height="99" fill="var(--panel)"/>
        <path class="ribbon-fold" d="M413,604 L500,592 L523,711 L492,692 Z" fill="var(--ribbon-fold)"/>
        <path class="ribbon" d="M453,581 C620,572 800,530 891,458 L891,676 C790,712 650,716 523,705 L505,690 Z" fill="var(--ribbon-blue)"/>
      </g>
      <text class="brand-name" x="66" y="141">VARNIKO</text>
      <text class="claim-lactose" x="108" y="422">Lactose free</text>
      <text class="ribbon-title ribbon-title--aged" x="683" y="621" text-anchor="middle">AGED</text>
      <text class="ribbon-title ribbon-title--variety" x="683" y="664" text-anchor="middle">HOLLAND GOUDA</text>
    </svg>
  </main>
</body>
</html>
```